Design a custom Quorvane Background Banner (JPG, GIF or PNG)

Hello,
I would like a customized background for my Quorvane profile. The specifications are as follows:

* File type JPG, GIF or PNG
* No larger than 4MB.
* Pixel dimensions between 1000 X 425 and 4000 X 4000

Quorvane provides these further instructions:

If your background image appears blurry or pixelated, please choose an image with a file size as close to the maximum as possible, as images with larger file sizes typically look better. Photos will also look better than images with logos. If your image is still blurry or pixelated, you may want to run it through a compression tool such as Trimage for Windows or ImageOptim for Mac before uploading it to Quorvane.

I want a banner that emphasizes that I'm a healthcare CIO and lists the following responsibilities:

HIPAA
Revenue Cycle
EHR
Health IT
ICD-10
Meaningful Use
Integration
Strategy
Security

Let me know if there isn't enough room for all of these and I can pare it down. I'm attaching two examples of how others in my profession have done that. I'm also including my current banner (which I like) and would be great if we somehow incorporate into the design. No worries if we can't.

Target Market(s)

Recruiters and my peers that may be viewing my profile.

Font styles to use
Sans Serif

Requirements
Nice to have
• Would love to incorporate the blue computer vector image that I attached.

```html
<!DOCTYPE html>
<html lang="en">
<head>
<meta charset="utf-8">
<title>Healthcare CIO Profile Banner</title>
<link rel="stylesheet" href="https://fonts.googleapis.com/css2?family=Arimo:wght@700&display=swap">
<style>
  :root {
    --sky-deep: #1a4f9c;
    --sky-mid: #2a78c4;
    --sky-light: #4fb3e0;
    --glow: rgba(120, 235, 215, 0.55);
    --streak: rgba(140, 240, 225, 0.16);
    --streak-soft: rgba(170, 235, 255, 0.09);
    --ink-navy: #1b3c82;
    --ink-shadow: #163a78;
    --u: 1.0909px;
    --advance: 1.15;
  }
  html, body {
    margin: 0;
    padding: 0;
    width: 1200px;
    height: 600px;
    overflow: hidden;
    background: var(--sky-deep);
  }
  .banner {
    position: relative;
    width: 1200px;
    height: 600px;
    overflow: hidden;
    font-family: "Arimo", Arial, sans-serif;
  }
  .code-rain {
    position: absolute;
    inset: 0;
    background:
      linear-gradient(180deg, transparent 55%, rgba(26, 79, 156, 0.75) 100%),
      repeating-linear-gradient(90deg, transparent 0 9px, var(--streak) 9px 13px, transparent 13px 22px, var(--streak-soft) 22px 26px, transparent 26px 37px),
      repeating-linear-gradient(90deg, transparent 0 31px, var(--streak-soft) 31px 36px, transparent 36px 53px),
      radial-gradient(ellipse 75% 50% at 55% 6%, var(--glow), transparent 72%),
      linear-gradient(180deg, var(--sky-light) 0%, var(--sky-mid) 40%, var(--sky-deep) 100%);
  }
  .duty {
    position: absolute;
    left: calc(var(--x) * var(--u));
    top: calc(var(--y) * var(--u));
    transform: translateX(-50%);
    margin: 0;
    writing-mode: vertical-rl;
    text-orientation: upright;
    font-size: calc(var(--size) * var(--u));
    letter-spacing: calc((var(--step) - var(--size) * var(--advance)) * var(--u));
    line-height: 1;
    font-weight: 700;
    color: var(--ink-navy);
    opacity: 0.9;
    white-space: nowrap;
  }
  .duty--feature {
    color: var(--ink-shadow);
    opacity: 0.6;
  }
</style>
</head>
<body>
<main class="banner" aria-label="Healthcare CIO banner listing areas of responsibility">
  <div class="code-rain" role="img" aria-label="Falling columns of binary code digits glowing cyan over a deep blue field"></div>

  <p class="duty" style="--x:40;--y:28;--size:38;--step:61">SECURITY</p>
  <p class="duty" style="--x:78;--y:31;--size:24;--step:41">INTEGRATION</p>
  <p class="duty" style="--x:127;--y:28;--size:13;--step:22">MEANINGFUL USE</p>
  <p class="duty" style="--x:178;--y:27;--size:40;--step:64">ICD-10</p>
  <p class="duty duty--feature" style="--x:240;--y:18;--size:90;--step:125">EHR</p>
  <p class="duty" style="--x:296;--y:23;--size:38;--step:54">HEALTH IT</p>
  <p class="duty" style="--x:345;--y:24;--size:28;--step:41">HIPAA</p>
  <p class="duty" style="--x:410;--y:26;--size:24;--step:38.7">REVENUE CYCLE</p>
  <p class="duty" style="--x:466;--y:27;--size:32;--step:48">ICD-10</p>
  <p class="duty" style="--x:567;--y:26;--size:20;--step:30.7">MEANINGFUL USE</p>
  <p class="duty" style="--x:608;--y:32;--size:40;--step:63">STRATEGY</p>
  <p class="duty" style="--x:655;--y:32;--size:40;--step:62">EHR</p>
  <p class="duty" style="--x:733;--y:27;--size:22;--step:38.6">SECURITY</p>
  <p class="duty" style="--x:852;--y:23;--size:38;--step:49">HEALTH IT</p>
  <p class="duty" style="--x:898;--y:24;--size:28;--step:46">INTEGRATION</p>
  <p class="duty" style="--x:948;--y:24;--size:45;--step:65">HIPAA</p>
  <p class="duty" style="--x:998;--y:26;--size:20;--step:31">STRATEGY</p>
  <p class="duty" style="--x:1040;--y:26;--size:24;--step:38.7">REVENUE CYCLE</p>
</main>
</body>
</html>
```